Business Card Design

A business card design must match as a cleaning company.
We do house cleaning, office, cafe , function center , club and so on.

Industry/Entity Type

House

Contact Information for Business Card

Bright Lane cleaning services
Mara Delvin
Director
0428395146
1300 917 254
Brightlane.cleaning@bluvex.com

```html
<!DOCTYPE html>
<html lang="en">
<head>
<meta charset="UTF-8">
<title>Bright Lane Cleaning Services – Business Card</title>
<link rel="stylesheet" href="https://fonts.googleapis.com/css2?family=Advent+Pro:wght@300;400&family=Ubuntu:wght@400;500;700&display=swap">
<style>
  :root {
    --page-bg: #e9e6e2;
    --card-dark: #2f281f;
    --card-mid: #4a4035;
    --accent: #f0a040;
    --accent-light: #f8b878;
    --accent-deep: #ee9530;
    --ink: #1e1a14;
    --subtitle: #e8e2da;
  }
  html, body {
    margin: 0;
    padding: 0;
    width: 1200px;
    height: 1000px;
    overflow: hidden;
    background: var(--page-bg);
  }
  .canvas {
    position: relative;
    width: 1200px;
    height: 1000px;
  }
  .card {
    position: absolute;
    left: 100px;
    top: 200px;
    width: 1000px;
    height: 600px;
    background:
      radial-gradient(ellipse 60% 55% at 50% 48%, var(--card-mid) 0%, var(--card-dark) 100%);
    box-shadow: 0 6px 20px rgba(0,0,0,0.25);
  }
  .brand {
    position: absolute;
    left: 0;
    right: 0;
    top: 148px;
    text-align: center;
  }
  .brand-name {
    margin: 0;
    font-family: "Advent Pro", sans-serif;
    font-weight: 300;
    font-size: 84px;
    line-height: 1;
    letter-spacing: 5px;
    color: var(--accent);
    text-transform: uppercase;
  }
  .brand-tagline {
    margin: 8px 0 0 18px;
    font-family: "Advent Pro", sans-serif;
    font-weight: 400;
    font-size: 31px;
    letter-spacing: 1.5px;
    color: var(--subtitle);
  }
  .info-band {
    position: absolute;
    left: 57px;
    top: 384px;
    width: 883px;
    height: 154px;
    border-top: 3px solid var(--accent);
    border-bottom: 3px solid var(--accent);
    box-sizing: border-box;
    padding: 5px 0;
    display: flex;
    gap: 8px;
  }
  .info-block {
    background: linear-gradient(135deg, var(--accent-light) 0%, var(--accent-deep) 100%);
    height: 100%;
  }
  .person {
    width: 437px;
    display: flex;
    flex-direction: column;
    align-items: center;
    justify-content: center;
    font-family: "Ubuntu", sans-serif;
    color: var(--ink);
  }
  .person-name {
    font-size: 38px;
    font-weight: 500;
    line-height: 1.1;
  }
  .person-role {
    font-size: 22px;
    font-weight: 500;
    margin-top: 4px;
  }
  .contact {
    flex: 1;
    display: flex;
    flex-direction: column;
    justify-content: center;
    gap: 14px;
    padding-left: 38px;
    font-family: "Ubuntu", sans-serif;
    font-size: 21px;
    color: var(--ink);
  }
  .contact-row {
    display: flex;
    align-items: center;
    gap: 14px;
    white-space: nowrap;
  }
  .contact-icon {
    width: 36px;
    height: 24px;
    flex: none;
  }
</style>
</head>
<body>
<main class="canvas">
  <section class="card" aria-label="Bright Lane cleaning services business card">
    <header class="brand">
      <h1 class="brand-name">Bright Lane</h1>
      <p class="brand-tagline">cleaning services</p>
    </header>

    <div class="info-band">
      <div class="info-block person">
        <span class="person-name">Mara Delvin</span>
        <span class="person-role">Director</span>
      </div>
      <div class="info-block contact">
        <div class="contact-row">
          <svg class="contact-icon" viewBox="0 0 36 24" aria-hidden="true">
            <path d="M2 7 C2 2 34 2 34 7 L34 9 L26 9 L26 6 L10 6 L10 9 L2 9 Z" fill="#1e1a14"/>
            <path d="M9 11 L27 11 L31 22 L5 22 Z" fill="#1e1a14"/>
            <circle cx="18" cy="16" r="3.2" fill="#f4a655"/>
          </svg>
          <span>0428395146/1300 917 254</span>
        </div>
        <div class="contact-row">
          <svg class="contact-icon" viewBox="0 0 36 24" aria-hidden="true">
            <rect x="4" y="3" width="28" height="18" fill="#1e1a14"/>
            <path d="M4 3 L18 14 L32 3" fill="none" stroke="#f4a655" stroke-width="1.6"/>
          </svg>
          <span>Brightlane.cleaning@bluvex.com</span>
        </div>
      </div>
    </div>
  </section>
</main>
</body>
</html>
```